Business Card Design Project

Please create a custom business card for Plume analytics. The logo is attached to this brief.

Address :
CEO : Baptiste Lorand
Mobile : +33641927508
14 rue Véronèse
75013 Paris
France

Reason: Sorry wrong logo. I will update asap

Hi, Sorry, I post the wrong file. I just update the correct logo. If you can integrate some charts as background it will be nice

Hi Everybody Please make it beautifull, clean, soft like pebble designs does to create their product. I want somewhere to show in a beautifull way some datavisualization charts. Not to much, but try to find a way to design it beautifull with less. Get inspire by datavisualization : http://www.morvelkit.com/48207-clean-vector-infographic-and-data-visualization-design-elements-03/

Target Market(s)

B to B
Customers are accountant, CPA, finance departement

Industry/Entity Type

Business

Font styles to use
Sans Serif

Requirements
Must have
• I want to give a clear message about what we do. We do dashboards, we create beautifull charts
Nice to have
• displays charts icons to let people know tha we do charts

```html
<!DOCTYPE html>
<html lang="fr">
<head>
<meta charset="utf-8">
<title>Plume analytics — carte de visite</title>
<link rel="stylesheet" href="https://fonts.googleapis.com/css2?family=Courier+Prime:wght@400;700&family=Montserrat:wght@400&display=swap">
<style>
  :root {
    --backdrop: #e6eaec;
    --card: #ffffff;
    --ink-navy: #1f3552;
    --ink-grey: #7d8794;
    --ink-soft: #a7b0ba;
    --card-shadow: rgba(31, 53, 82, 0.14);
  }
  html, body {
    margin: 0;
    width: 1200px;
    height: 817px;
    overflow: hidden;
    background: var(--backdrop);
  }
  .stage {
    width: 1200px;
    height: 817px;
    display: flex;
    align-items: center;
    justify-content: center;
  }
  .business-card {
    position: relative;
    width: 840px;
    height: 480px;
    background: var(--card);
    box-shadow: 0 18px 40px var(--card-shadow);
  }
  .brand {
    position: absolute;
    top: 112px;
    right: 70px;
    text-align: left;
    display: flex;
    align-items: center;
    gap: 18px;
  }
  .brand-mark {
    width: 22px;
    height: 22px;
    border-radius: 50%;
    background: var(--ink-navy);
  }
  .brand-text { display: flex; flex-direction: column; gap: 8px; }
  .brand-name {
    font-family: "Montserrat", sans-serif;
    font-weight: 400;
    font-size: 40px;
    letter-spacing: 0.5px;
    color: var(--ink-navy);
    line-height: 1;
  }
  .brand-tagline {
    font-family: "Montserrat", sans-serif;
    font-size: 13px;
    letter-spacing: 1px;
    color: var(--ink-soft);
  }
  .contact {
    position: absolute;
    left: 62px;
    bottom: 58px;
    font-family: "Courier Prime", monospace;
    color: var(--ink-grey);
  }
  .contact-name {
    margin: 0 0 8px;
    font-weight: 700;
    font-size: 19px;
    color: var(--ink-navy);
  }
  .contact-lines {
    margin: 0;
    padding: 0;
    list-style: none;
    font-size: 12px;
    line-height: 1.45;
  }
</style>
</head>
<body>
  <main class="stage">
    <article class="business-card">
      <div class="brand">
        <span class="brand-mark"></span>
        <div class="brand-text">
          <span class="brand-name">Plume analytics</span>
          <span class="brand-tagline">Dashboards &amp; data charts</span>
        </div>
      </div>
      <div class="contact">
        <p class="contact-name">Baptiste Lorand</p>
        <ul class="contact-lines">
          <li>CEO</li>
          <li>+33641927508</li>
          <li>14 rue Véronèse</li>
          <li>75013 Paris</li>
          <li>France</li>
        </ul>
      </div>
    </article>
  </main>
</body>
</html>
```